Meadowgate Counselling Group Pty Ltd

clinical psychologist in private practice needs professional stationery package: business cards, complimentary slips, envelopes, range of business letterheads, and logo (photo of lighthouse).

I work with children, adolescents, adults and older population with a range of mental health concerns, adjustment to life transitions and learning difficulties. Majority of my correspondence is with medical practitioners writing reports. I would a clean crisp professional presentation (white background, navy blue text but open to ideas). Thought about having lighthouse as watermark on envelopes. My professional organisation (KRV) logo needs to be on business cards and templates (manual gives guidelines),. The photo of lighthouse is to be included in logo.
There needs to be three letterheads. 1.Is Company only Detail "meadowgate Counselling Group Pty Ltd". 2. Include Company detail and Fiona Hartwell Clinical Psychologist information at BQTG. 3. Include Company detail and Fiona Hartwell Clinical Psychologist information at Corran Vale Medical Centre

Target Market(s)

Doctors

Industry/Entity Type

Business

Colors
0355a3
3176b5
0592cd
33a6d7

Requirements
Must have
• Picture of the lighthouse
• KRV logo
• Business name

```html
<!DOCTYPE html>
<html lang="en">
<head>
<meta charset="utf-8">
<title>Meadowgate Counselling Group – Stationery</title>
<link rel="stylesheet" href="https://fonts.googleapis.com/css2?family=Tinos:wght@400;700&family=Open+Sans:wght@400;600;700&display=swap">
<style>
  :root{
    --navy:#0355a3;
    --navy-deep:#0b3f8c;
    --blue:#3176b5;
    --sky:#0592cd;
    --sky-light:#33a6d7;
    --ink:#1f2a36;
    --rule:#9aa6b4;
    --paper:#ffffff;
    --stage:#eceff2;
  }
  *{box-sizing:border-box;margin:0;padding:0}
  html,body{width:1200px;height:931px;overflow:hidden;background:var(--stage)}
  .stage{position:relative;width:1200px;height:931px;overflow:hidden;font-family:"Open Sans",Arial,sans-serif;color:var(--ink)}
  .sheet{position:absolute;background:var(--paper);box-shadow:0 1px 3px rgba(0,0,0,.12);overflow:hidden}
  .serif{font-family:"Tinos","Times New Roman",serif}

  /* logo */
  .logo{position:absolute;display:flex;align-items:flex-start}
  .logo-photo{flex:none;border:1px solid var(--navy-deep);background:linear-gradient(180deg,#7fb3e3 0%,#b9d6ef 55%,#8d9aa3 85%,#6d7b84 100%)}
  .logo-name{font-family:"Tinos","Times New Roman",serif;font-weight:400;color:var(--navy);margin-left:6px}
  .logo-abn{position:absolute;font-size:6.5px;color:#111;white-space:nowrap}

  .band-text{position:absolute;color:#fff;white-space:nowrap}
  .tagline{color:var(--sky);text-align:right;font-family:"Tinos","Times New Roman",serif;line-height:1.1}

  /* letterhead */
  .letterhead{left:100px;top:58px;width:480px;height:684px}
  .lh-person{position:absolute;right:22px;top:20px;text-align:right}
  .lh-person .name{font-size:13px;font-weight:700;color:var(--navy-deep)}
  .lh-person .role{font-size:10px;color:var(--blue);margin-top:1px}
  .lh-person .cred{font-size:6px;color:#222;line-height:9px;margin-top:3px}
  .lh-bar{position:absolute;right:0;top:22px;width:4px;height:62px;background:var(--navy)}
  .letter-body{position:absolute;left:53px;top:193px;width:372px;font-size:7.2px;line-height:10px;color:#111}
  .letter-body .salute{font-weight:700;color:var(--navy);margin-bottom:18px}
  .letter-body p{margin-bottom:10px}
  .sign-off{margin-top:30px}
  .sign-off b{display:block}
  .signature{width:90px;height:44px;margin-top:6px;background:linear-gradient(90deg,rgba(3,85,163,.12),rgba(3,85,163,.04))}

  .contact-row{position:absolute;display:flex;font-size:6.8px;line-height:9px;color:#111;white-space:nowrap}
  .contact-row .col{padding:0 6px;border-left:1px solid var(--rule)}
  .contact-row .col:first-child{border-left:none;padding-left:0}
  .contact-row .label{color:var(--blue);font-weight:600;font-size:8px;line-height:10px}
  .lh-contacts{font-size:5.7px;line-height:8.5px;letter-spacing:-.05px}
  .lh-contacts .col{padding:0 5px}
  .lh-contacts .stack{padding-top:10px;line-height:9.5px}
  .ico{display:inline-block;width:7px;height:7px;border-radius:50%;background:var(--blue);vertical-align:-1px;margin-right:4px;position:relative}
  .ico::after{content:"";position:absolute;left:2px;top:2px;width:3px;height:3px;border-radius:50%;background:#fff}
  .lh-contacts .ico{width:6px;height:6px;margin-right:3px}
  .lh-contacts .ico::after{left:1.5px;top:1.5px}
  .member{position:absolute;display:flex;align-items:center;gap:4px;color:#fff;font-size:11px}
  .member i{display:block;width:13px;height:13px;border-radius:50%;border:1.5px solid #fff}

  .wave{position:absolute;left:0;bottom:0;width:100%}

  /* envelope back */
  .env-back{left:626px;top:58px;width:540px;height:260px}

  /* dl front + comp slip */
  .env-front{left:626px;top:338px;width:540px;height:259px}
  .comp-slip{left:626px;top:645px;width:540px;height:259px}
  .return-addr{position:absolute;left:24px;top:108px;font-size:10px;color:#111}
  .with-comp{position:absolute;right:28px;top:20px;font-size:14px;font-weight:700;color:var(--navy-deep)}
  .slip-person{position:absolute;right:28px;top:174px;text-align:right}
  .slip-person .name{font-size:11px;font-weight:700;color:var(--navy-deep)}
  .slip-person .role{font-size:9px;color:var(--blue)}

  /* business cards */
  .card{top:778px;width:220px;height:124px}
  .card-front{left:100px}
  .card-back{left:345px}
  .card-person{position:absolute;right:12px;top:40px;text-align:right}
  .card-person .name{font-size:8px;font-weight:700;color:var(--navy-deep)}
  .card-person .role,.card-person .cred{font-size:5.5px;color:var(--blue)}
  .card-person .cred{color:#222}
  .card-contact{position:absolute;left:12px;top:66px;font-size:5px;line-height:7.5px;color:#111}
  .card-addr{position:absolute;right:12px;top:72px;font-size:5.5px;line-height:7px;text-align:right;color:#111}
  .appt-head{position:absolute;left:12px;top:10px;font-size:6.5px;font-weight:700;color:var(--navy-deep);line-height:7px;display:flex;gap:5px}
  .appt-head i{width:5px;height:5px;background:var(--navy);display:block;margin-top:1px}
  .appt-form{position:absolute;left:12px;right:12px;top:36px;font-size:5.5px;color:var(--navy-deep)}
  .appt-form .line{display:flex;align-items:flex-end;height:11px;gap:3px}
  .appt-form .fill{flex:1;border-bottom:.6px solid var(--blue);height:6px}
  .days{display:flex;justify-content:space-between;height:11px;align-items:center}
  .days span::before{content:"";display:inline-block;width:4px;height:4px;border:.6px solid var(--navy-deep);margin-right:2px;vertical-align:-.5px}
  .appt-foot{position:absolute;left:0;right:0;bottom:0;height:12px;background:var(--navy);color:#fff;font-size:4.8px;line-height:12px;text-align:center}
</style>
</head>
<body>
<div class="stage">

  <!-- LETTERHEAD -->
  <section class="sheet letterhead">
    <div class="logo" style="left:30px;top:24px">
      <div class="logo-photo" role="img" aria-label="Photograph of a white lighthouse against a blue sky" style="width:52px;height:74px"></div>
      <div class="logo-name" style="font-size:20px;line-height:19px">Meadowgate<br>Counselling<br>Group Pty Ltd</div>
    </div>
    <div class="logo-abn" style="left:88px;top:88px">ABN: 48 302 715 964</div>

    <div class="lh-person">
      <div class="name serif">Fiona Hartwell</div>
      <div class="role serif">Clinical Psychologist</div>
      <div class="cred">MEd.MPsych(Clinical).MKRV<br>AHPRA #PSY000487315<br>Medicare Provider # 7720415K &amp; 7720417M<br>Email: fiona.psy@mailhaven.com</div>
    </div>
    <div class="lh-bar"></div>
    <div class="tagline" style="position:absolute;right:12px;top:91px;font-size:10px">Therapy and assessment for<br>children, adolescents and adults</div>

    <article class="letter-body">
      <div class="salute">Dear Mr. Alan Reed</div>
      <p>Lorem ipsum dolor sit amet, consectetuer adipiscing elit. Aenean commodo ligula eget dolor. Aenean massa. Cum sociis natoque penatibus et magnis dis parturient montes, nascetur ridiculus mus. Donec quam felis, ultricies nec, pellentesque eu, pretium quis, sem. Nulla consequat massa quis enim. Donec pede justo, fringilla vel, aliquet nec, vulputate eget, arcu.</p>
      <p style="margin-top:14px">In enim justo, rhoncus ut, imperdiet a, venenatis vitae, justo. Nullam dictum felis eu pede mollis pretium. Integer tincidunt. Cras dapibus. Vivamus elementum semper nisi. Aenean vulputate eleifend tellus. Aenean leo ligula, porttitor eu, consequat vitae, eleifend ac, enim. Aliquam lorem ante, dapibus in, viverra quis, feugiat a, tellus.</p>
      <p style="margin-top:14px">Phasellus viverra nulla ut metus varius laoreet. Quisque rutrum. Aenean imperdiet. Etiam ultricies nisi vel augue. Curabitur ullamcorper ultricies nisi. Nam eget dui. Etiam rhoncus. Maecenas tempus, tellus eget condimentum rhoncus, sem quam semper libero, sit amet adipiscing sem neque sed ipsum. Nam quam nunc, blandit vel, luctus pulvinar, hendrerit id, lorem. Maecenas nec odio et ante tincidunt tempus. Donec vitae sapien ut libero venenatis faucibus. Nullam quis ante. Etiam sit amet orci eget eros faucibus tincidunt. Duis leo. Sed fringilla mauris sit amet nibh. Donec sodales sagittis magna. Sed consequat, leo eget bibendum sodales, augue velit cursus nunc,</p>
      <div class="sign-off"><b>Sincerely,</b>Morgan<br>General Manager</div>
      <div class="signature" role="img" aria-label="Handwritten signature"></div>
    </article>

    <div class="contact-row lh-contacts" style="left:17px;top:592px">
      <div class="col"><div class="label">Clinics:</div>Bellmore Quay Therapy, Suite 6<br>12 Ardent St, WESTLEIGH QLD 4391</div>
      <div class="col"><div class="label">Clinics:</div>Corran Vale Medical Centre<br>47 Tarrant Rd, CORRAN VALE QLD 4377</div>
      <div class="col"><div class="label">Mail:</div>PO Box 318,<br>FERNHOLT QLD 4368</div>
      <div class="col stack"><span class="ico"></span>07 5512 3907<br><span class="ico"></span>07 5512 3918</div>
      <div class="col stack"><span class="ico"></span>admin@bqtg.com.au<br><span class="ico"></span>www.bqtg.com.au</div>
    </div>

    <svg class="wave" width="480" height="62" viewBox="0 0 480 62" preserveAspectRatio="none" aria-hidden="true">
      <defs>
        <linearGradient id="bandA" x1="0" x2="1" y1="0" y2="0">
          <stop offset="0" stop-color="#0b3f8c"/><stop offset=".5" stop-color="#0355a3"/><stop offset="1" stop-color="#0b3f8c"/>
        </linearGradient>
      </defs>
      <path d="M0,24 C150,22 320,16 480,2 L480,62 L0,62 Z" fill="url(#bandA)"/>
      <path d="M0,8 C110,20 230,20 360,12 C240,24 110,26 0,16 Z" fill="#33a6d7"/>
      <path d="M0,18 C150,24 320,18 480,4 L480,7 C320,21 150,27 0,22 Z" fill="#3176b5" opacity=".6"/>
    </svg>
    <div class="band-text" style="left:24px;top:662px;font-size:10px">Navigating life’s challenges: learning, wellbeing, relationships, and change.</div>
    <div class="member" style="right:24px;top:646px"><i></i>KRV</div>
  </section>

  <!-- ENVELOPE BACK -->
  <section class="sheet env-back">
    <svg width="540" height="260" viewBox="0 0 540 260" aria-hidden="true" style="position:absolute;inset:0">
      <path d="M12,0 L24,90 L516,90 L528,0" fill="none" stroke="#dde1e5" stroke-width="1"/>
    </svg>
  </section>

  <!-- DL ENVELOPE FRONT -->
  <section class="sheet env-front">
    <div class="logo" style="left:24px;top:27px">
      <div class="logo-photo" role="img" aria-label="Photograph of a white lighthouse against a blue sky" style="width:48px;height:68px"></div>
      <div class="logo-name" style="font-size:19px;line-height:18px">Meadowgate<br>Counselling<br>Group Pty Ltd</div>
    </div>
    <div class="logo-abn" style="left:78px;top:86px">ABN: 48 302 715 964</div>
    <div class="tagline" style="position:absolute;right:14px;top:25px;font-size:10.5px">Therapy and assessment for<br>children, adolescents and adults</div>
    <div class="return-addr">PO Box 318, FERNHOLT QLD 4368</div>
    <svg class="wave" width="540" height="58" viewBox="0 0 540 58" preserveAspectRatio="none" aria-hidden="true">
      <defs>
        <linearGradient id="bandB" x1="0" x2="1"><stop offset="0" stop-color="#0b3f8c"/><stop offset=".5" stop-color="#0355a3"/><stop offset="1" stop-color="#0b3f8c"/></linearGradient>
      </defs>
      <path d="M0,20 C170,20 360,14 540,2 L540,58 L0,58 Z" fill="url(#bandB)"/>
      <path d="M0,4 C120,16 250,16 270,12 C250,20 120,22 0,12 Z" fill="#33a6d7"/>
    </svg>
    <div class="band-text" style="left:93px;top:236px;font-size:10.5px">Navigating life’s challenges: learning, wellbeing, relationships, and change.</div>
  </section>

  <!-- COMPLIMENTS SLIP -->
  <section class="sheet comp-slip">
    <div class="logo" style="left:24px;top:27px">
      <div class="logo-photo" role="img" aria-label="Photograph of a white lighthouse against a blue sky" style="width:48px;height:68px"></div>
      <div class="logo-name" style="font-size:19px;line-height:18px">Meadowgate<br>Counselling<br>Group Pty Ltd</div>
    </div>
    <div class="logo-abn" style="left:78px;top:86px">ABN: 48 302 715 964</div>
    <div class="with-comp">With Compliments</div>
    <div class="tagline" style="position:absolute;right:28px;top:46px;font-size:10.5px">Therapy and assessment for<br>children, adolescents and adults</div>
    <div class="contact-row" style="left:22px;top:177px;font-size:7px;line-height:11px">
      <div class="col">Suite 6, 12 Ardent St<br>Westleigh QLD 4391</div>
      <div class="col"><span class="ico"></span>07 5512 3907<br><span class="ico"></span>07 5512 3918</div>
      <div class="col"><span class="ico"></span>admin@bqtg.com.au<br><span class="ico"></span>www.bqtg.com.au</div>
    </div>
    <div class="slip-person serif"><div class="name">Fiona Hartwell</div><div class="role">Clinical Psychologist</div></div>
    <svg class="wave" width="540" height="58" viewBox="0 0 540 58" preserveAspectRatio="none" aria-hidden="true">
      <defs>
        <linearGradient id="bandC" x1="0" x2="1"><stop offset="0" stop-color="#0b3f8c"/><stop offset=".5" stop-color="#0355a3"/><stop offset="1" stop-color="#0b3f8c"/></linearGradient>
      </defs>
      <path d="M0,20 C170,20 360,14 540,2 L540,58 L0,58 Z" fill="url(#bandC)"/>
      <path d="M0,4 C120,16 250,16 270,12 C250,20 120,22 0,12 Z" fill="#33a6d7"/>
    </svg>
    <div class="band-text" style="left:93px;top:236px;font-size:10.5px">Navigating life’s challenges: learning, wellbeing, relationships, and change.</div>
  </section>

  <!-- BUSINESS CARD FRONT -->
  <section class="sheet card card-front">
    <div class="logo" style="left:12px;top:10px">
      <div class="logo-photo" role="img" aria-label="Photograph of a white lighthouse against a blue sky" style="width:22px;height:34px"></div>
      <div class="logo-name" style="font-size:10px;line-height:10px;margin-left:4px">Meadowgate<br>Counselling<br>Group Pty Ltd</div>
    </div>
    <div class="logo-abn" style="left:38px;top:40px;font-size:3.5px">ABN: 48 302 715 964</div>
    <div class="tagline" style="position:absolute;right:12px;top:10px;font-size:6px">Therapy and assessment for<br>children, adolescents and adults</div>
    <div class="card-person serif"><div class="name">Fiona Hartwell</div><div class="role">Clinical Psychologist</div><div class="cred">MEd.MPsych(Clinical).MKRV</div></div>
    <div class="card-contact"><span class="ico" style="width:4px;height:4px"></span>07 5512 3907<br><span class="ico" style="width:4px;height:4px"></span>07 5512 3918<br><span class="ico" style="width:4px;height:4px"></span>admin@bqtg.com.au<br><span class="ico" style="width:4px;height:4px"></span>www.bqtg.com.au</div>
    <div class="card-addr">Suite 6, 12 Ardent St<br>Westleigh QLD 4391</div>
    <svg class="wave" width="220" height="26" viewBox="0 0 220 26" preserveAspectRatio="none" aria-hidden="true">
      <path d="M0,12 C70,11 150,8 220,1 L220,26 L0,26 Z" fill="#0355a3"/>
      <path d="M0,4 C50,9 100,9 120,7 C100,11 50,12 0,8 Z" fill="#33a6d7"/>
    </svg>
    <div class="band-text" style="left:12px;top:113px;font-size:4.6px">Navigating life’s challenges: learning, wellbeing, relationships, and change.</div>
    <div class="member" style="right:10px;top:106px;font-size:6px;gap:2px"><i style="width:7px;height:7px;border-width:1px"></i>KRV</div>
  </section>

  <!-- BUSINESS CARD BACK -->
  <section class="sheet card card-back">
    <div class="appt-head"><i></i><span>Next<br>Appointment</span></div>
    <div class="card-person serif" style="top:10px"><div class="name">Fiona Hartwell</div><div class="role">Clinical Psychologist</div></div>
    <div class="appt-form">
      <div class="line">Name:<span class="fill"></span></div>
      <div class="days"><span>MON.</span><span>TUE.</span><span>WED.</span><span>THURS.</span><span>FRI.</span><span>SAT.</span></div>
      <div class="line">Date:<span class="fill"></span>Time:<span class="fill"></span>A.M. / P.M.</div>
      <div class="line">Notes:<span class="fill"></span></div>
      <div class="line"><span class="fill"></span></div>
      <div class="line"><span class="fill"></span></div>
    </div>
    <div class="appt-foot">If you are unable to attend, please inform us as soon as possible. <b>Ph: (07) 5512 3907</b></div>
  </section>

</div>
</body>
</html>
```